Webbanner-Design für Führungskräfte-Coach
Danke für Ihr Engagement und die einwandfreie Abwicklung.
Zielgruppe
Ich coache Führungskräfte und Teams im Verkauf. Haupt-Keywort und Haupt-Thema:
Führung im Vertrieb. Das Design soll Führungskräften mit Verkaufsfunktionen gefallen.
Aufgabenstellung
Gemäss Memo (Datei: RBF-Banner-Memo).

```html
<!DOCTYPE html>
<html lang="de">
<head>
<meta charset="utf-8">
<title>RBF Coaching &amp; Training – Webbanner</title>
<link rel="stylesheet" href="https://fonts.googleapis.com/css2?family=Open+Sans:ital,wght@0,400;0,600;1,400&display=swap">
<style>
  :root {
    --page-bg: #e9ebee;
    --panel-left: #d9dbe5;
    --panel-right: #d3d5e1;
    --ink: #1d1f26;
    --ink-soft: #3a3d48;
    --accent-red: #d0212b;
    --logo-band: rgba(240, 241, 246, 0.82);
    --photo-top: #c9ccd6;
    --photo-mid: #8f96a6;
    --photo-low: #4a5060;
  }
  * { margin: 0; padding: 0; box-sizing: border-box; }
  html, body {
    width: 1200px;
    height: 2213px;
    overflow: hidden;
    background: var(--page-bg);
    font-family: "Open Sans", Arial, sans-serif;
    color: var(--ink);
  }
  .banner {
    position: absolute;
    left: 50px;
    top: 896px;
    width: 1100px;
    height: 421px;
    display: flex;
    box-shadow: 0 1px 3px rgba(0,0,0,0.18);
  }
  .banner__quote {
    width: 234px;
    background: var(--panel-left);
    padding: 124px 14px 0 20px;
    position: relative;
  }
  .quote__text {
    font-style: italic;
    font-size: 15.5px;
    line-height: 28px;
    color: var(--ink);
  }
  .quote__author {
    font-style: italic;
    font-size: 14px;
    text-align: right;
    margin-top: 10px;
    padding-right: 12px;
  }
  .banner__visual {
    width: 630px;
    position: relative;
    overflow: hidden;
  }
  .visual__photo {
    position: absolute;
    inset: 0;
    background:
      radial-gradient(ellipse 38% 70% at 66% 55%, #5c6374 0%, rgba(92,99,116,0) 70%),
      linear-gradient(180deg, var(--photo-top) 0%, var(--photo-mid) 50%, var(--photo-low) 100%);
  }
  .visual__logo {
    position: absolute;
    left: 0;
    right: 0;
    top: 39px;
    height: 84px;
    background: var(--logo-band);
    display: flex;
    align-items: center;
    padding-left: 14px;
    gap: 12px;
  }
  .logo__mark {
    width: 40px;
    height: 40px;
    background: var(--accent-red);
  }
  .logo__name {
    font-size: 21px;
    font-weight: 600;
    line-height: 1.05;
    color: var(--ink);
  }
  .logo__name small {
    display: block;
    font-size: 16px;
    font-weight: 600;
    color: var(--ink);
  }
  .visual__headline {
    position: absolute;
    left: 0;
    right: 0;
    bottom: 24px;
    text-align: center;
    font-size: 24px;
    color: var(--ink);
    text-shadow: 0 0 8px rgba(255,255,255,0.7);
  }
  .banner__topics {
    width: 236px;
    background: var(--panel-right);
    padding: 40px 10px 0 14px;
    list-style: none;
  }
  .topic {
    position: relative;
    padding-left: 10px;
    font-size: 18.5px;
    line-height: 23px;
    color: var(--ink-soft);
    margin-bottom: 23px;
  }
  .topic::before {
    content: "";
    position: absolute;
    left: 0;
    top: 10px;
    width: 4px;
    height: 4px;
    border-radius: 50%;
    background: var(--accent-red);
  }
</style>
</head>
<body>
  <section class="banner" aria-label="Webbanner RBF Coaching &amp; Training">
    <div class="banner__quote">
      <p class="quote__text">„Als Businesscoach und Trainer unterstütze ich Unternehmen dabei, wie sie Ergebnisse im Umgang mit Kunden verbessern und die Kompetenzen dazu kontinuierlich trainieren.“</p>
      <p class="quote__author">Rolf Brandt</p>
    </div>

    <div class="banner__visual">
      <div class="visual__photo" role="img" aria-label="Foto: Coach im Anzug vor einem unscharfen Verkaufsteam im Büro"></div>
      <div class="visual__logo">
        <span class="logo__mark"></span>
        <p class="logo__name">RBF<small>Coaching &amp; Training GmbH</small></p>
      </div>
      <p class="visual__headline">Coach für Führungskräfte und Teams im Vertrieb</p>
    </div>

    <ul class="banner__topics">
      <li class="topic">Führungs-System und strategische Vorgaben</li>
      <li class="topic">Bildungskonzept und Ausbildungsstandards</li>
      <li class="topic">Produktive Prozesse</li>
      <li class="topic">Verkaufskompetenzen</li>
      <li class="topic">Leadership-Kompetenzen</li>
      <li class="topic">Ständiger Lern- und Verbesserungsprozess</li>
    </ul>
  </section>
</body>
</html>
```